Signage for Brightwell Academy - Exterior

Size 32 ft x 5 ft 11 inches. It will be installed at a height of 25 feet. Should contain the Logo, Address, some courses to give an idea about what we do. The signage is installed on the 2nd floor, so the minimum size of letters would be as in the old signage design attached. The font size of the bottom line of our existing signage is as small as we should go. Basically it should be such that the first glance gives us an idea that it is a Brightwell Academy. You are allowed to change the logo colors, but the font and design will remain the same.
Updates

Reason: some extra time might be needed to improve the designs and get new inputs. need some out of the box designing.

Target Market(s)

High School and College going teens who wish to learn software skills for graphics and animation

Industry/Entity Type

Education

Font styles to use
Other font styles liked:
• Utopia

Colors

Designer to choose colors to be used in the design.

Requirements
Must have
• Logo, Address, Phone Number, website address, what we do.
• 1. Please refer to the image of our old signage uploaded. The font size of the courses mentioned at the bottom of the signage "ANIMATION, GAMING.." is the smallest size which is legible from the ground level.
• 2. We would like at least the web address in legible font size and if possible the phone number too. The physical address could be a little smaller as in the old signage, as that is not a calling factor and in case someone is interested, they can walk closer and read the address.
• 3. The calling factors would be a few courses and some graphics depicting what we do in the first look.
• 4.You are allowed to change the logo colors, but the font and design will remain the same. Prefer usage of Ubuntu font for text.
• 5. Prefer minimalist look and not cluttered. I feel mentioning more courses is making the signage cluttered. we can limit it to 3 courses.
Nice to have
• Graphics to suggest what we do. It should be eye catching. The graphic should be such that speaks of what we do. It should be suggestive.
Should not have
• It should not be too busy

```html
<!DOCTYPE html>
<html lang="en">
<head>
<meta charset="utf-8">
<title>Brightwell Academy – Exterior Signage</title>
<link href="https://fonts.googleapis.com/css2?family=Ubuntu:wght@400;500;700&display=swap" rel="stylesheet">
<style>
  :root {
    --navy: #1d3962;
    --beam: #2f8fe0;
    --beam-light: #5fb6f2;
    --white: #ffffff;
    --curtain: #9e1016;
    --rule: #ffffff;
  }
  * { margin: 0; padding: 0; box-sizing: border-box; }
  html, body {
    width: 1200px; height: 224px; overflow: hidden;
    background: var(--navy);
  }
  .signage {
    position: relative; width: 1200px; height: 224px; overflow: hidden;
    background: var(--navy);
    font-family: "Ubuntu", sans-serif; color: var(--white);
  }
  .backdrop { position: absolute; inset: 0; }
  .side-area {
    position: absolute; top: 0; width: 118px; height: 224px;
    background: var(--curtain);
  }
  .side-area--left { left: 0; }
  .side-area--right { right: 0; }

  .courses {
    position: absolute; left: 110px; width: 220px; top: 62px;
    text-align: center; font-weight: 700; font-size: 29px;
    line-height: 46px; letter-spacing: 0.5px; text-transform: uppercase;
  }
  .brand {
    position: absolute; left: 340px; width: 340px; top: 66px;
    text-align: center; font-weight: 500; color: var(--white);
    text-transform: uppercase; line-height: 1;
  }
  .brand__line { display: block; font-size: 52px; letter-spacing: 2px; }
  .brand__line + .brand__line { margin-top: 22px; letter-spacing: 10px; }

  .services {
    position: absolute; left: 680px; width: 150px; top: 64px;
    text-align: center; font-weight: 700; font-size: 29px;
    line-height: 47px; text-transform: uppercase;
  }
  .divider {
    position: absolute; left: 836px; top: 38px; width: 1.5px; height: 166px;
    background: var(--rule);
  }
  .contact { position: absolute; left: 860px; top: 36px; }
  .contact__row {
    display: flex; align-items: center; gap: 6px;
    font-weight: 700; font-size: 21px; height: 32px; letter-spacing: 0.3px;
  }
  .contact__icon { width: 17px; height: 17px; flex: none; }
  .address { margin-top: 10px; font-size: 15.5px; line-height: 24.5px; font-weight: 400; }
  .address__city { font-weight: 700; font-size: 17px; }
</style>
</head>
<body>
<div class="signage">
  <svg class="backdrop" width="1200" height="224" viewBox="0 0 1200 224" aria-hidden="true">
    <defs>
      <linearGradient id="beamLeft" x1="0" y1="1" x2="1" y2="0">
        <stop offset="0" stop-color="var(--beam-light)"/>
        <stop offset="0.6" stop-color="var(--beam)"/>
        <stop offset="1" stop-color="var(--navy)" stop-opacity="0"/>
      </linearGradient>
      <linearGradient id="beamRight" x1="1" y1="1" x2="0" y2="0">
        <stop offset="0" stop-color="var(--beam-light)"/>
        <stop offset="0.6" stop-color="var(--beam)"/>
        <stop offset="1" stop-color="var(--navy)" stop-opacity="0"/>
      </linearGradient>
    </defs>
    <polygon points="100,55 380,224 100,224" fill="url(#beamLeft)" opacity="0.9"/>
    <polygon points="100,110 290,224 100,224" fill="var(--beam-light)" opacity="0.35"/>
    <polygon points="1100,60 790,224 1100,224" fill="url(#beamRight)" opacity="0.9"/>
    <polygon points="1100,120 900,224 1100,224" fill="var(--beam-light)" opacity="0.35"/>
  </svg>

  <div class="side-area side-area--left" role="img" aria-label="Red stage curtain on the left edge"></div>
  <div class="side-area side-area--right" role="img" aria-label="Red stage curtain on the right edge"></div>

  <div class="courses">
    <div>Animation</div>
    <div>Film Making</div>
    <div>VFX</div>
  </div>

  <div class="brand">
    <span class="brand__line">Brightwell</span>
    <span class="brand__line">Academy</span>
  </div>

  <div class="services">
    <div>Web &amp;</div>
    <div>Graphic</div>
    <div>Design</div>
  </div>

  <div class="divider"></div>

  <div class="contact">
    <div class="contact__row">
      <svg class="contact__icon" viewBox="0 0 20 20" aria-hidden="true">
        <circle cx="10" cy="10" r="8.5" fill="none" stroke="#fff" stroke-width="1.8"/>
        <ellipse cx="10" cy="10" rx="3.5" ry="8.5" fill="none" stroke="#fff" stroke-width="1.4"/>
        <line x1="1.5" y1="10" x2="18.5" y2="10" stroke="#fff" stroke-width="1.4"/>
      </svg>
      <span>BRIGHTWELL.IN</span>
    </div>
    <div class="contact__row">
      <svg class="contact__icon" viewBox="0 0 20 20" aria-hidden="true">
        <circle cx="10" cy="10" r="8.5" fill="none" stroke="#fff" stroke-width="1.8"/>
        <path d="M7,5.5 L8.6,5.3 L9.3,8 L8.2,8.8 C8.8,10.2 9.8,11.2 11.2,11.8 L12,10.7 L14.7,11.4 L14.5,13 C11,13.3 6.7,9 7,5.5 Z" fill="#fff"/>
      </svg>
      <span>91 172 555 0147</span>
    </div>
    <div class="address">
      <div class="address__city">CHANDIGARH</div>
      <div>SCO 12-13, First Floor</div>
      <div>Sector 21 B</div>
      <div>P: 0172 555 0147</div>
    </div>
  </div>
</div>
</body>
</html>
```